Vessa Almond Protein - simply made, well made

Design a protein powder pouch (350g). Take inspiration from Brimora.co and put the same information on the pouch and add "made in Australia". I do not want it to be exactly the same design but just take some inspiration from it.

```html
<!DOCTYPE html>
<html lang="en">
<head>
<meta charset="utf-8">
<title>Vessa Almond Protein Pouches</title>
<link rel="stylesheet" href="https://fonts.googleapis.com/css2?family=Open+Sans:wght@400;600;700&display=swap">
<style>
  :root {
    --backdrop: #ece6df;
    --cream: #efe9dc;
    --ink: #2b2b2b;
    --choc-top: #2f5b47;
    --choc-bottom: #6a3c25;
    --choc-left: #b27f5a;
    --choc-right: #58301b;
    --choc-label: #7a4a38;
    --choc-foot: #f1e6da;
    --van-top: #6a9a80;
    --van-bottom: #88a993;
    --van-left: #d9c18b;
    --van-right: #d98e2b;
    --van-label: #e0903a;
    --van-foot: #eef2ea;
    --flag: #27408b;
  }
  * { margin: 0; padding: 0; box-sizing: border-box; }
  html, body { width: 1200px; height: 1200px; overflow: hidden; }
  body {
    background: var(--backdrop);
    font-family: "Open Sans", sans-serif;
    position: relative;
  }
  .pouch {
    position: absolute;
    top: 187px;
    width: 510px;
    height: 856px;
    color: var(--ink);
    text-align: center;
  }
  .pouch--chocolate {
    left: 64px;
    --top: var(--choc-top); --bottom: var(--choc-bottom);
    --left-wedge: var(--choc-left); --right-wedge: var(--choc-right);
    --label: var(--choc-label); --foot: var(--choc-foot);
  }
  .pouch--vanilla {
    left: 627px;
    --top: var(--van-top); --bottom: var(--van-bottom);
    --left-wedge: var(--van-left); --right-wedge: var(--van-right);
    --label: var(--van-label); --foot: var(--van-foot);
  }
  .pouch-shape { position: absolute; inset: 0; }
  .pouch-shape .band-top { fill: var(--top); }
  .pouch-shape .band-mid { fill: var(--cream); }
  .pouch-shape .band-bottom { fill: var(--bottom); }
  .pouch-shape .wedge-left { fill: var(--left-wedge); }
  .pouch-shape .wedge-right { fill: var(--right-wedge); }
  .pouch-shape .zip { stroke: rgba(0,0,0,0.14); stroke-width: 2; fill: none; }
  .pouch-shape .notch { fill: var(--backdrop); }
  .brand {
    position: absolute; left: 0; right: 0; top: 150px;
    font-weight: 700; font-size: 54px; line-height: 1;
    color: #f2efe8; letter-spacing: 0.5px;
  }
  .tagline {
    position: absolute; left: 0; right: 0; top: 210px;
    font-size: 15px; color: #e8e6df; letter-spacing: 0.8px;
  }
  .product-name {
    position: absolute; left: 0; right: 0; top: 330px;
    font-weight: 700; font-size: 47px; line-height: 52px;
    letter-spacing: 1px; color: #2f2f2f;
  }
  .flavour {
    position: absolute; left: 50%; top: 499px; transform: translateX(-50%);
    width: 240px; height: 31px; line-height: 31px;
    background: var(--label); color: #f6efe6;
    font-size: 18px; letter-spacing: 1.2px;
  }
  .features {
    position: absolute; left: 0; right: 0; top: 564px;
    font-size: 18px; color: #2f2f2f;
  }
  .benefits-title {
    position: absolute; left: 0; right: 0; top: 684px;
    font-size: 18px; color: var(--foot);
  }
  .benefits {
    position: absolute; left: 0; right: 0; top: 716px;
    font-size: 16px; color: var(--foot);
  }
  .net-weight {
    position: absolute; left: 0; right: 0; top: 765px;
    font-size: 16px; color: var(--foot);
  }
  .origin {
    position: absolute; left: 0; right: 0; top: 796px;
    font-size: 16px; color: var(--foot);
  }
  .flag {
    display: inline-block; width: 20px; height: 12px; margin-left: 8px;
    background: var(--flag); vertical-align: middle;
  }
</style>
</head>
<body>

<section class="pouch pouch--chocolate">
  <svg class="pouch-shape" viewBox="0 0 510 856" width="510" height="856">
    <rect class="band-mid" x="0" y="0" width="510" height="856"/>
    <rect class="band-top" x="0" y="0" width="510" height="294"/>
    <polygon class="wedge-left" points="0,363 130,500 0,700"/>
    <polygon class="wedge-right" points="510,294 370,421 510,520"/>
    <polygon class="band-bottom" points="0,667 510,597 510,856 0,856"/>
    <line class="zip" x1="20" y1="100" x2="490" y2="100"/>
    <rect class="notch" x="0" y="56" width="8" height="4"/>
    <rect class="notch" x="502" y="56" width="8" height="4"/>
  </svg>
  <div class="brand">Vessa</div>
  <div class="tagline">simply made, well made</div>
  <h1 class="product-name">ALMOND<br>PROTEIN<br>POWDER</h1>
  <div class="flavour">REAL CHOCOLATE</div>
  <p class="features">Vegan · Just 4 Ingredients · Delicious</p>
  <p class="benefits-title">Naturally Supports Health:</p>
  <p class="benefits">Heart · Digestion · Immune · Skin · Bone · Hair</p>
  <p class="net-weight">Net Wt. 350g</p>
  <p class="origin">Made in Australia<span class="flag" role="img" aria-label="Australian flag"></span></p>
</section>

<section class="pouch pouch--vanilla">
  <svg class="pouch-shape" viewBox="0 0 510 856" width="510" height="856">
    <rect class="band-mid" x="0" y="0" width="510" height="856"/>
    <rect class="band-top" x="0" y="0" width="510" height="294"/>
    <polygon class="wedge-left" points="0,363 110,500 0,700"/>
    <polygon class="wedge-right" points="510,294 380,430 510,520"/>
    <polygon class="band-bottom" points="0,667 510,597 510,856 0,856"/>
    <line class="zip" x1="20" y1="100" x2="490" y2="100"/>
    <rect class="notch" x="0" y="56" width="8" height="4"/>
    <rect class="notch" x="502" y="56" width="8" height="4"/>
  </svg>
  <div class="brand">Vessa</div>
  <div class="tagline">simply made, well made</div>
  <h1 class="product-name">ALMOND<br>PROTEIN<br>POWDER</h1>
  <div class="flavour">REAL VANILLA</div>
  <p class="features">Vegan · Just 4 Ingredients · Delicious</p>
  <p class="benefits-title">Naturally Supports Health:</p>
  <p class="benefits">Heart · Digestion · Immune · Skin · Bone · Hair</p>
  <p class="net-weight">Net Wt. 350g</p>
  <p class="origin">Made in Australia<span class="flag" role="img" aria-label="Australian flag"></span></p>
</section>

</body>
</html>
```